Web Design Company Needs New Look

We are a very, very busy web development company that doesn't have the time to look after our own website because of the workload. Now the site has become stale and an afterthought. I need a designer that can deliver a home page template, basic inside page template and portfolio template that will be fresh, amazing looking, and show off the qualities clients love about us.
I want strong imagery that I can help choose (although your input would be greatly appreciated), amazing fonts, clean-clean-clean and really , really need to lean on a great creative designer that can take the lead on this as we have very minimal time available due to our workload.
It Company

```html
<!DOCTYPE html>
<html lang="en">
<head>
<meta charset="utf-8">
<title>Lumen – Internet Solutions</title>
<link rel="stylesheet" href="https://fonts.googleapis.com/css2?family=Arvo:wght@400;700&family=Didact+Gothic&family=Maven+Pro:wght@400&family=PT+Sans:wght@400&display=swap">
<style>
  :root {
    --black: #050505;
    --stripe: #8fa9bb;
    --hero-dark: #1a2634;
    --hero-mid: #3a4a5c;
    --paper: #f2f2f2;
    --ink: #2b3440;
    --body: #3d3d3d;
    --steel: #5a7b91;
    --steel-light: #8aa8bd;
    --button: #7d9db2;
    --circle: #a9c1d2;
    --white: #ffffff;
    --link: #7fb6dc;
    --tab: #9aa6ae;
  }
  * { margin: 0; padding: 0; box-sizing: border-box; }
  html, body { width: 836px; height: 1200px; overflow: hidden; background: var(--black); }
  .page { position: relative; width: 836px; height: 1200px; font-family: "PT Sans", sans-serif; }

  .site-header { position: absolute; top: 0; left: 0; width: 836px; height: 54px; background: var(--black); }
  .brand { position: absolute; left: 129px; top: 8px; font-family: "Maven Pro", sans-serif; font-size: 31px; color: var(--steel-light); letter-spacing: 0.5px; }
  .main-nav { position: absolute; left: 313px; top: 21px; display: flex; gap: 6px; font-family: "Didact Gothic", sans-serif; font-size: 8.6px; color: var(--white); }
  .main-nav span.sep { color: var(--steel-light); }

  .stripe { position: absolute; left: 0; width: 836px; height: 8px; background: var(--stripe); border-top: 1px dashed #c7d6e0; border-bottom: 1px dashed #c7d6e0; }

  .hero { position: absolute; top: 62px; left: 0; width: 836px; height: 426px;
    background: radial-gradient(ellipse 260px 120px at 170px 40px, #5b6570 0%, transparent 100%),
                radial-gradient(ellipse 300px 260px at 420px 220px, var(--hero-mid) 0%, var(--hero-dark) 100%); }
  .hero-kicker { position: absolute; top: 25px; width: 100%; text-align: center; font-family: "Arvo", serif; font-size: 20px; color: var(--white); }
  .hero-title { position: absolute; top: 48px; width: 100%; text-align: center; font-family: "Arvo", serif; font-weight: 700; font-size: 35px; color: #eef2f5; letter-spacing: 1px; }
  .hero-showcase { position: absolute; left: 270px; top: 116px; width: 296px; height: 250px; border-radius: 6px;
    background: linear-gradient(180deg, #1b1b1b 0%, #111 52%, #e9e9e9 72%, #cfcfcf 100%); }
  .slider-dots { position: absolute; top: 385px; left: 395px; display: flex; gap: 6px; }
  .slider-dots i { width: 11px; height: 11px; border-radius: 50%; background: #050505; display: block; }
  .slider-dots i.active { background: var(--button); }

  .welcome { position: absolute; top: 488px; left: 0; width: 836px; height: 311px; background: var(--paper); text-align: center; }
  .welcome-kicker { position: absolute; top: 23px; width: 100%; font-family: "Arvo", serif; font-size: 18px; color: var(--ink); }
  .welcome-title { position: absolute; top: 44px; width: 100%; font-family: "Arvo", serif; font-weight: 700; font-size: 25px; color: var(--ink); letter-spacing: 0.5px; }
  .welcome-portrait { position: absolute; left: 362px; top: 82px; width: 112px; height: 112px; border-radius: 50%; background: radial-gradient(circle at 50% 45%, #5a5f66, #2e3238); }
  .welcome-text { position: absolute; top: 211px; left: 170px; width: 496px; font-size: 8px; line-height: 10.8px; color: var(--body); }
  .btn { position: absolute; height: 16px; width: 47px; background: var(--button); color: var(--white); font-family: "Didact Gothic", sans-serif; font-size: 7.5px; line-height: 16px; text-align: center; border-radius: 2px; }

  .services { position: absolute; top: 799px; left: 0; width: 836px; height: 326px; background: var(--steel); }
  .services-title { position: absolute; left: 131px; top: 25px; font-family: "Arvo", serif; font-weight: 700; font-size: 23px; color: var(--white); letter-spacing: 0.5px; }
  .services-text { position: absolute; left: 131px; top: 59px; width: 252px; font-size: 8px; line-height: 10.8px; color: var(--white); }
  .service-path { position: absolute; left: 0; top: 0; }
  .service-label { position: absolute; left: 183px; top: 254px; width: 94px; height: 16px; background: var(--circle); color: var(--white); font-size: 7.8px; line-height: 16px; text-align: center; }
  .testimonial-title { position: absolute; left: 455px; top: 205px; font-family: "Arvo", serif; font-weight: 700; font-size: 14px; color: var(--white); }
  .testimonial-quote { position: absolute; left: 475px; top: 229px; width: 222px; font-size: 8px; line-height: 10.8px; color: var(--white); }
  .quote-mark { position: absolute; font-family: "Arvo", serif; font-size: 20px; color: var(--steel-light); }
  .testimonial-author { position: absolute; right: 152px; top: 280px; font-family: "Arvo", serif; font-size: 10px; color: var(--white); }

  .site-footer { position: absolute; top: 1133px; left: 0; width: 836px; height: 67px; background: var(--black); }
  .footer-nav { position: absolute; left: 131px; top: 17px; font-size: 8px; color: var(--link); }
  .footer-nav span.sep { color: #aaa; margin: 0 5px; }
  .footer-legal { position: absolute; left: 131px; top: 29px; font-size: 8px; color: var(--link); }
  .social { position: absolute; left: 644px; top: 17px; display: flex; gap: 4px; }
  .social i { display: block; width: 18px; height: 18px; border-radius: 50%; background: var(--steel-light); }
  .support-tab { position: absolute; left: 720px; top: 47px; width: 88px; height: 20px; background: var(--tab); border-radius: 2px 2px 0 0; font-family: "Didact Gothic", sans-serif; font-size: 7.5px; color: #222; line-height: 20px; padding-left: 9px; }
  .support-tab::after { content: ""; position: absolute; right: 8px; top: 8px; border: 3.5px solid transparent; border-bottom: 4px solid #222; }
</style>
</head>
<body>
<div class="page">
  <header class="site-header">
    <div class="brand">Lumen</div>
    <nav class="main-nav">
      <span>HOME</span><span class="sep">•</span><span>OUR COMPANY</span><span class="sep">•</span><span>SERVICES</span><span class="sep">•</span><span>PORTFOLIO</span><span class="sep">•</span><span>FREE RESOURCES</span><span class="sep">•</span><span>PAY ONLINE</span><span class="sep">•</span><span>CONTACT US</span>
    </nav>
  </header>
  <div class="stripe" style="top:54px"></div>

  <section class="hero">
    <p class="hero-kicker">INTERNET SOLUTIONS</p>
    <h1 class="hero-title">WEB DESIGNING</h1>
    <div class="hero-showcase" role="img" aria-label="Desktop monitor showing a fashion shop website project"></div>
    <div class="slider-dots"><i class="active"></i><i></i><i></i></div>
  </section>

  <section class="welcome">
    <p class="welcome-kicker">WELCOME TO LUMEN</p>
    <h2 class="welcome-title">WHY CHOOSE LUMEN</h2>
    <div class="welcome-portrait" role="img" aria-label="Portrait photo of a cheerful businessman making a victory sign"></div>
    <p class="welcome-text">90% of our projects are started by referrals or repeat clients.<br>Think about that for a moment. Nearly every new project we start is by a client that was so happy with our previous work that they want to work with us again. Even our new contacts are from previous clients referring us to them. Simply put, clients love our work and recommend us time and time again.</p>
    <div class="btn" style="left:395px;top:268px">MORE</div>
  </section>

  <section class="services">
    <h2 class="services-title">OUR SERVICES</h2>
    <p class="services-text">Let’s face it – your website is the first thing that a business associate or consumer will see when they search for your product or service online. Lumen Internet Solutions combines the best quality and design to make sure that what your customers see accurately reflects your business. You may be one of the largest companies on the east-ern seaboard or the corner store in a small town</p>
    <div class="btn" style="left:131px;top:133px">MORE</div>

    <svg class="service-path" width="836" height="326" viewBox="0 0 836 326">
      <path d="M152 262 C175 252 178 228 205 222 L318 203 C360 190 385 178 405 165 L450 138 C475 122 485 112 495 108 L540 88 C560 80 575 77 590 74 L628 70 C640 82 645 64 655 60" fill="none" stroke="#2f4656" stroke-width="1" stroke-dasharray="3 2"/>
      <circle cx="230" cy="217" r="30" fill="var(--circle)"/>
      <path d="M228 247 l6 6 l6 -6 z" fill="var(--circle)"/>
      <circle cx="230" cy="217" r="18" fill="none" stroke="#fff" stroke-width="3"/>
      <circle cx="333" cy="200" r="30" fill="var(--circle)"/>
      <g fill="none" stroke="#fff" stroke-width="3" stroke-linecap="round"><path d="M346 187 L322 211 a4 4 0 0 1 -6 -6 L340 181"/><path d="M338 179 l10 10"/></g>
      <circle cx="423" cy="154" r="30" fill="var(--circle)"/>
      <g fill="none" stroke="#fff" stroke-width="2.6" stroke-linejoin="round"><path d="M408 148 h30 l-4 17 h-22 z"/><path d="M415 147 l8 -10 l8 10"/><path d="M418 152 v9 M423 152 v9 M428 152 v9"/></g>
      <circle cx="507" cy="103" r="30" fill="var(--circle)"/>
      <g fill="none" stroke="#fff" stroke-width="3" stroke-linecap="round"><circle cx="511" cy="98" r="11"/><path d="M503 106 l-10 10"/></g>
      <circle cx="601" cy="72" r="30" fill="var(--circle)"/>
      <g fill="none" stroke="#fff" stroke-width="2.6"><circle cx="601" cy="72" r="18"/><path d="M590 65 L608 60 L612 80 L594 83 Z"/><circle cx="608" cy="60" r="3" fill="#fff"/><circle cx="594" cy="83" r="3" fill="#fff"/></g>
    </svg>
    <div class="service-label">SiteCraft Websites</div>

    <h3 class="testimonial-title">TESTIMONIAL</h3>
    <span class="quote-mark" style="left:455px;top:222px">“</span>
    <p class="testimonial-quote">Lorem Ipsum is simply dummy text of the printing and typesetting industry. Lorem Ipsum has been the industry’s standard dummy text ever since the 1500s,</p>
    <span class="quote-mark" style="left:688px;top:252px">”</span>
    <p class="testimonial-author">By Dr. Halvorsen</p>
  </section>

  <div class="stripe" style="top:1125px"></div>

  <footer class="site-footer">
    <nav class="footer-nav">Home<span class="sep">|</span>Our Company<span class="sep">|</span>Services<span class="sep">|</span>Portfolio<span class="sep">|</span>Free Resources<span class="sep">|</span>Pay Online<span class="sep">|</span>Contact Us</nav>
    <p class="footer-legal">Lumen © 2013 • Privacy Policy</p>
    <div class="social"><i></i><i></i><i></i></div>
    <div class="support-tab">ONLINE SUPPORT</div>
  </footer>
</div>
</body>
</html>
```